Packaging Artwork for "Earth's First Expanding Biodisposable Loofah Pads"

Our company manufactures BrisaPods. They are Earth's first expanding, biodisposable loofah pads for exfoliating the skin.
BrisaPods are biodisposable, so they can be thrown-away (or composted) before nasty skin bacteria can grow on them. This makes scrubbing skin cleaner and safer.
This is a high-end product, so our packaging needs to be very clean, sophisticated and make our product look like it should be expensive. The packaging should also let the viewer know the product is environmentally friendly.
The product name is "BrisaPods". The packaging also has to say "Biodisposable".
Our new packaging is a hanging bag with a window in it. See the image attached. There is also a picture of our current packaging for our Tarnivelles sponges. We would like completely different artwork, but keep the white paper.
The attached images are of our kitchen cleaning pads "Quorlimates". This new packaging is for "BrisaPods" which are a beauty product and the artwork must be different. Also, the packaging should have a large image of the round loofah pad on the front and the image of the loofah expanding from thin to thick on the back.
Updates

This will be a 4-inch x 4-inch bag that will hang from a hook. The bag will be about 2-inches thick. The logo will be similar to the Quorlimates fish logo that has been added to the project. Instead of saying "tarnivelles", the word "BrisaPods" needs to be used in the logo.

Industry/Entity Type

health and beauty

Requirements
Must have
• slogan "Clean Germ Free. Guilt Free". The product should be called "Earth's First Expanding Biodisposable Bath Loofahs". simple clean design on a white background. see the picture of our current packaging below. We will use the same paper. We just need completely different, sophisticated artwork

```html
<!DOCTYPE html>
<html lang="en">
<head>
<meta charset="utf-8">
<title>BrisaPods – Biodisposable Pack Front</title>
<link rel="stylesheet" href="https://fonts.googleapis.com/css2?family=Nunito:wght@400;600;700;800&family=Roboto:wght@400;500;700&family=Roboto+Condensed:wght@700&display=swap">
<style>
  :root {
    --backdrop: #2b2b2c;
    --paper: #ffffff;
    --teal: #72b5ae;
    --sage: #a6d0a8;
    --deep-teal: #1c9a97;
    --ocean-blue: #0a73bd;
    --cocoa: #6b5b5b;
  }
  html, body {
    margin: 0;
    padding: 0;
    width: 1200px;
    height: 1200px;
    overflow: hidden;
    background: var(--backdrop);
  }
  .pack-front {
    position: absolute;
    left: 112px;
    top: 112px;
    width: 1220px;
    height: 1220px;
    transform: scale(0.8);
    transform-origin: top left;
    background: var(--paper);
    overflow: hidden;
    font-family: "Nunito", sans-serif;
  }
  .waves {
    position: absolute;
    inset: 0;
    width: 1220px;
    height: 1220px;
  }
  .pack-count {
    position: absolute;
    left: 804px;
    top: 48px;
    font-family: "Roboto", sans-serif;
    font-weight: 400;
    font-size: 104px;
    line-height: 1;
    color: var(--teal);
    letter-spacing: -4px;
  }
  .pack-count-label {
    position: absolute;
    left: 914px;
    top: 68px;
    font-weight: 700;
    font-size: 31px;
    line-height: 35px;
    color: var(--ocean-blue);
  }
  .supply {
    position: absolute;
    left: 807px;
    top: 148px;
    font-family: "Roboto Condensed", sans-serif;
    font-weight: 700;
    font-size: 29px;
    line-height: 1;
    color: var(--teal);
  }
  .benefits {
    position: absolute;
    left: 808px;
    top: 211px;
    margin: 0;
    padding: 0;
    list-style: none;
  }
  .benefit {
    display: flex;
    align-items: center;
    height: 86px;
    margin-bottom: 11px;
    font-weight: 600;
    font-size: 32px;
    color: var(--teal);
  }
  .benefit::before {
    content: "";
    width: 85px;
    height: 85px;
    border-radius: 50%;
    background: var(--teal);
    margin-right: 15px;
    flex: none;
  }
  .brand {
    position: absolute;
    left: 110px;
    top: 520px;
    display: flex;
    align-items: center;
  }
  .brand-dot {
    width: 90px;
    height: 90px;
    border-radius: 50%;
    background: var(--teal);
    margin-right: 24px;
  }
  .brand-name {
    font-weight: 800;
    font-size: 124px;
    line-height: 1;
    color: var(--cocoa);
    letter-spacing: -1px;
  }
  .product-type {
    position: absolute;
    left: 112px;
    top: 838px;
    font-weight: 800;
    font-size: 110px;
    line-height: 1;
    color: var(--cocoa);
  }
  .slogan-band {
    position: absolute;
    left: 0;
    top: 992px;
    width: 1220px;
    height: 96px;
    background: var(--ocean-blue);
    display: flex;
    align-items: center;
    justify-content: center;
    font-family: "Roboto", sans-serif;
    font-weight: 500;
    font-size: 46px;
    color: var(--paper);
    letter-spacing: -0.5px;
  }
</style>
</head>
<body>
  <main class="pack-front">
    <svg class="waves" viewBox="0 0 1220 1220" aria-hidden="true">
      <path d="M0,0 H960 C500,30 150,150 0,420 Z" fill="var(--teal)"/>
      <path d="M0,0 H600 C350,20 150,60 0,110 Z" fill="var(--sage)"/>
      <path d="M1220,700 C1100,1000 700,1160 30,1220 H1220 Z" fill="var(--teal)"/>
      <path d="M1220,1085 C1000,1180 700,1210 300,1220 H1220 Z" fill="var(--sage)"/>
      <circle cx="1163" cy="927" r="10" fill="var(--deep-teal)"/>
      <circle cx="778" cy="1132" r="20" fill="var(--deep-teal)"/>
      <circle cx="880" cy="1150" r="15" fill="var(--deep-teal)"/>
      <circle cx="1014" cy="1154" r="29" fill="var(--deep-teal)"/>
      <circle cx="1119" cy="1124" r="15" fill="var(--deep-teal)"/>
    </svg>

    <div class="pack-count">12</div>
    <div class="pack-count-label">Expanding<br>loofah pads</div>
    <div class="supply">3 MONTH SUPPLY</div>

    <ul class="benefits">
      <li class="benefit">All plant</li>
      <li class="benefit">Tough</li>
      <li class="benefit">Biodegradable</li>
    </ul>

    <div class="brand">
      <span class="brand-dot"></span>
      <span class="brand-name">BrisaPods</span>
    </div>

    <div class="product-type">Biodisposable</div>

    <div class="slogan-band">CLEAN GERM FREE. GUILT FREE.</div>
  </main>
</body>
</html>
```